Letterhead and Stationary for Construction Company

Brisk Current needs modern Letterhead, Envelopes and Notepad designs.

Industry/Entity Type

Construction

Colors
f78f20
34a7d8
ffffff

Requirements
Must have
• Modern looking design.

```html
<!DOCTYPE html>
<html lang="en">
<head>
<meta charset="utf-8">
<title>Brisk Current Stationery</title>
<link href="https://fonts.googleapis.com/css2?family=Montserrat:wght@600&family=Roboto:wght@400;500&display=swap" rel="stylesheet">
<style>
  :root {
    --brand-blue: #1677bd;
    --brand-orange: #f78f20;
    --paper: #ffffff;
    --ink: #3a3a3a;
    --rule: #b9b9b9;
    --backdrop: #1c1c1c;
  }
  html, body {
    margin: 0;
    width: 1200px;
    height: 960px;
    overflow: hidden;
    background: var(--backdrop);
  }
  .canvas { position: relative; width: 1200px; height: 960px; }
  .sheet {
    position: absolute;
    background: var(--paper);
    box-shadow: 0 4px 10px rgba(0,0,0,.55);
  }
  .wordmark {
    display: flex;
    align-items: center;
    gap: 6px;
    font-family: "Montserrat", sans-serif;
    font-weight: 600;
    color: var(--brand-blue);
    white-space: nowrap;
    line-height: 1;
  }
  .wordmark .dot {
    border-radius: 50%;
    background: var(--brand-orange);
    flex: none;
  }
  .contact {
    font-family: "Roboto", sans-serif;
    font-weight: 500;
    color: var(--ink);
    font-size: 5.5px;
    line-height: 1.35;
  }

  /* Letterhead */
  .letterhead { left: 63px; top: 212px; width: 408px; height: 527px; }
  .letterhead .wordmark { position: absolute; left: 34px; top: 44px; font-size: 19px; }
  .letterhead .wordmark .dot { width: 18px; height: 18px; }
  .letterhead .contact-block {
    position: absolute; left: 302px; top: 31px;
    border-left: 1px solid var(--rule);
    padding-left: 9px;
  }
  .letterhead .contact-block p { margin: 0; }
  .letterhead .contact-lines { margin-top: 5px; }
  .contact-lines p { display: flex; align-items: center; gap: 3px; }
  .contact-lines svg { width: 5px; height: 5px; flex: none; }

  /* Envelope back */
  .envelope-back { left: 503px; top: 342px; width: 408px; height: 186px; }
  .envelope-back .flap { position: absolute; left: 0; top: 0; width: 408px; height: 60px; }
  .envelope-back .flap-mark {
    position: absolute; left: 0; top: 18px; width: 408px;
    display: flex; justify-content: center;
  }
  .envelope-back .flap-mark .wordmark { color: var(--paper); font-size: 13px; }

  /* Envelope front */
  .envelope-front { left: 503px; top: 552px; width: 408px; height: 187px; }
  .envelope-front .wordmark { position: absolute; left: 16px; top: 22px; font-size: 16px; }
  .envelope-front .wordmark .dot { width: 14px; height: 14px; }
  .envelope-front .contact { position: absolute; left: 47px; top: 53px; }
  .envelope-front .contact p { margin: 0; }

  /* Folder cover */
  .folder-cover { left: 944px; top: 213px; width: 183px; height: 252px; background: var(--brand-blue); }
  .folder-cover .wordmark { position: absolute; left: 0; width: 183px; top: 114px; justify-content: center; color: var(--paper); font-size: 16px; }
  .folder-cover .web {
    position: absolute; left: 0; width: 183px; top: 231px; text-align: center;
    font-family: "Roboto", sans-serif; font-weight: 500; font-size: 5.5px;
    color: var(--paper); letter-spacing: .5px;
  }

  /* Notepad */
  .notepad { left: 946px; top: 487px; width: 183px; height: 252px; }
  .notepad .wordmark { position: absolute; left: 14px; top: 20px; font-size: 9px; gap: 4px; }
  .notepad .wordmark .dot { width: 9px; height: 9px; }
  .notepad .contact { position: absolute; right: 14px; top: 18px; text-align: right; font-size: 5px; }
  .notepad .contact p { margin: 0; }
  .notepad .ruled {
    position: absolute; left: 14px; right: 14px; top: 52px; height: 181px;
    background: repeating-linear-gradient(to bottom, var(--rule) 0 1px, transparent 1px 9.5px);
  }
</style>
</head>
<body>
<main class="canvas">

  <section class="sheet letterhead" aria-label="Letterhead">
    <div class="wordmark"><span class="dot"></span>Brisk Current</div>
    <div class="contact contact-block">
      <p>48 Harbor Lane, Kestrel</p>
      <p>P.O. Box 210, 318 Ridge</p>
      <div class="contact-lines">
        <p><svg viewBox="0 0 10 10"><path d="M2 1h2l1 2.5-1.3 1a6 6 0 0 0 2.8 2.8l1-1.3L10 7v2c0 .6-.4 1-1 1A9 9 0 0 1 0 1c0-.6.4-1 1-1z" fill="#f78f20"/></svg>555-0142-7781</p>
        <p><svg viewBox="0 0 10 10"><rect x="0" y="2" width="10" height="6.5" rx="1" fill="#f78f20"/><path d="M0.5 2.5 5 6l4.5-3.5" stroke="#fff" fill="none" stroke-width="1"/></svg>hello@briskcurrent.com</p>
        <p><svg viewBox="0 0 10 10"><circle cx="5" cy="5" r="4.3" fill="none" stroke="#f78f20" stroke-width="1.2"/><path d="M0.7 5h8.6M5 .7c-2.5 2.5-2.5 6.1 0 8.6M5 .7c2.5 2.5 2.5 6.1 0 8.6" stroke="#f78f20" fill="none" stroke-width=".8"/></svg>www.briskcurrent.com</p>
      </div>
    </div>
  </section>

  <section class="sheet envelope-back" aria-label="Envelope back">
    <svg class="flap" viewBox="0 0 408 60" aria-hidden="true">
      <path d="M0 0H408V10C405 30 404 54 392 58H16C4 54 3 30 0 10Z" fill="#1677bd"/>
    </svg>
    <div class="flap-mark"><div class="wordmark">Brisk Current</div></div>
  </section>

  <section class="sheet envelope-front" aria-label="Envelope front">
    <div class="wordmark"><span class="dot"></span>Brisk Current</div>
    <div class="contact">
      <p>48 Harbor Lane, Kestrel</p>
      <p>P.O. Box 210, 318 Ridge</p>
    </div>
  </section>

  <section class="sheet folder-cover" aria-label="Folder cover">
    <div class="wordmark">Brisk Current</div>
    <div class="web">www.briskcurrent.com</div>
  </section>

  <section class="sheet notepad" aria-label="Notepad">
    <div class="wordmark"><span class="dot"></span>Brisk Current</div>
    <div class="contact">
      <p>48 Harbor Lane, Kestrel</p>
      <p>P.O. Box 210, 318 Ridge</p>
    </div>
    <div class="ruled"></div>
  </section>

</main>
</body>
</html>
```